Business Card Design Project - Amber Keystone

Our company is in the fine arts and luxury collectibles insurance industry. We're looking for a clean business card design that will be on a 32pt business card. The business card should align with our branding strategy document, logo and word mark that was uploaded. We'll be looking to design a brochure as well.

Target Market(s)

Collector of fine art, coins, sports memorabilia and more

Industry/Entity Type

Insurance

Contact Information for Business Card

The design should be simple, elegant and sophisticated aligning with our brand.

Font styles to use
Other font styles liked:
• Source Sans Pro

Colors
33a6d7

Requirements
Must have
• Name - Derek Vollan
• Title - President
• Number - 555.217.8614 x0047
• Address - 2800 Fennimore Ave., Suite 410 Harbor Vista, NV 90000
• Email - derekv@tallpine-ins.com
• License - CA 0K83926
• Website - tallpine-ins.com
• Color Palette matching our brand platform - Reference attached document to see RGB, HEX or CMYK
Nice to have
• na
Should not have
• na

```html
<!DOCTYPE html>
<html lang="en">
<head>
<meta charset="utf-8">
<title>Tallpine Insurance — Business Card</title>
<link href="https://fonts.googleapis.com/css2?family=Source+Sans+3:wght@400;600;700&display=swap" rel="stylesheet">
<style>
  :root {
    --brand-blue: #33a6d7;
    --ink: #1f1f1f;
    --paper: #fbfbf9;
    --backdrop: #e6e6e4;
    --on-blue: #ffffff;
  }
  * { margin: 0; padding: 0; box-sizing: border-box; }
  html, body {
    width: 1200px; height: 801px; overflow: hidden;
    background: var(--backdrop);
    font-family: "Source Sans 3", "Source Sans Pro", sans-serif;
  }
  .canvas {
    position: relative; width: 1200px; height: 801px;
    display: flex; align-items: center; justify-content: center; gap: 70px;
  }
  .card { box-shadow: 0 6px 18px rgba(0,0,0,0.12); }
  .card-front {
    position: relative;
    width: 300px; height: 525px;
    background: var(--brand-blue);
  }
  .website {
    position: absolute; left: 40px; bottom: 48px;
    color: var(--on-blue); font-size: 17px; letter-spacing: 0.04em;
  }
  .website strong { font-weight: 600; }
  .card-back {
    position: relative;
    width: 600px; height: 343px;
    background: var(--paper);
    color: var(--ink);
  }
  .wordmark {
    position: absolute; top: 46px; right: 40px;
    display: flex; align-items: center; gap: 14px;
  }
  .wordmark-square { width: 50px; height: 50px; background: var(--brand-blue); }
  .wordmark-text {
    font-size: 30px; font-weight: 600; line-height: 1;
    color: var(--ink); letter-spacing: 0.01em;
  }
  .contact {
    position: absolute; left: 44px; bottom: 34px;
    font-size: 15px; line-height: 1.45;
  }
  .contact-name {
    font-size: 21px; font-weight: 700; text-transform: uppercase; line-height: 1.1;
  }
  .contact-title { font-size: 14px; text-transform: uppercase; margin-bottom: 10px; }
  .contact-line { display: flex; align-items: center; gap: 10px; }
  .contact-line svg { width: 13px; height: 13px; fill: var(--ink); flex: none; }
  .contact-address { margin-top: 4px; }
</style>
</head>
<body>
<main class="canvas">
  <section class="card card-front">
    <p class="website">www.<strong>tallpine-ins</strong>.com</p>
  </section>

  <section class="card card-back">
    <div class="wordmark">
      <span class="wordmark-square"></span>
      <span class="wordmark-text">Tallpine Insurance</span>
    </div>

    <div class="contact">
      <p class="contact-name">Derek Vollan</p>
      <p class="contact-title">President</p>
      <p class="contact-line">
        <svg viewBox="0 0 16 16" aria-hidden="true"><path d="M4 0h8a1 1 0 0 1 1 1v14a1 1 0 0 1-1 1H4a1 1 0 0 1-1-1V1a1 1 0 0 1 1-1zm1 2v10h6V2zm3 11a1 1 0 1 0 0 2 1 1 0 0 0 0-2z"/></svg>
        555.304.7721
      </p>
      <p class="contact-line">
        <svg viewBox="0 0 16 16" aria-hidden="true"><path d="M3.6 0.5l2.2 3-1.3 1.8c.9 2 2.3 3.5 4.3 4.4l1.8-1.3 3 2.2-1 3.4C6.5 13.8 1.8 9 0.3 1.6z"/></svg>
        555.217.8614 x0047
      </p>
      <p class="contact-line">
        <svg viewBox="0 0 16 16" aria-hidden="true"><path d="M0 3h16v1.2L8 9 0 4.2zm0 2.6l8 4.8 8-4.8V13H0z"/></svg>
        derekv@tallpine-ins.com
      </p>
      <p class="contact-address">2800 Fennimore Ave., Suite 410 Harbor Vista, NV 90000</p>
      <p>License - CA 0K83926</p>
    </div>
  </section>
</main>
</body>
</html>
```